Letterhead and Stationary for Construction Company

Brisk Current needs modern Letterhead, Envelopes and Notepad designs.

Industry/Entity Type

Construction

Colors
f78f20
34a7d8
ffffff

Requirements
Must have
• Modern looking design.

```html
<!DOCTYPE html>
<html lang="en">
<head>
<meta charset="utf-8">
<title>Brisk Current Letterhead</title>
<link href="https://fonts.googleapis.com/css2?family=Source+Sans+3:wght@300;400;600;700&display=swap" rel="stylesheet">
<style>
  :root {
    --orange: #f07726;
    --orange-dark: #c8632a;
    --blue: #0f76c0;
    --blue-mid: #1b5e99;
    --blue-deep: #134d80;
    --ink: #231f20;
    --body: #4d4d4d;
    --paper: #ffffff;
  }
  * { margin: 0; padding: 0; box-sizing: border-box; }
  html, body { width: 848px; height: 1200px; overflow: hidden; background: var(--paper); }
  body { font-family: "Source Sans 3", "Myriad Pro", Arial, sans-serif; color: var(--body); }
  .letterhead { position: relative; width: 848px; height: 1200px; overflow: hidden; background: var(--paper); }
  .accents { position: absolute; inset: 0; width: 848px; height: 1200px; }
  .brand { position: absolute; left: 98px; top: 118px; display: flex; align-items: center; gap: 10px; }
  .brand-dot { width: 20px; height: 20px; border-radius: 50%; background: var(--orange); }
  .brand-name { font-size: 32px; font-weight: 600; color: var(--orange); letter-spacing: -0.5px; line-height: 1; }
  .recipient { position: absolute; left: 105px; top: 365px; color: var(--ink); }
  .recipient-line { font-size: 16.5px; line-height: 20px; font-weight: 300; }
  .recipient-name { color: var(--blue); font-weight: 700; }
  .recipient-role, .sender-role { font-size: 11.5px; font-weight: 700; color: var(--ink); line-height: 15px; }
  .date { position: absolute; left: 614px; top: 366px; font-size: 13px; font-weight: 300; color: var(--body); }
  .letter-body { position: absolute; left: 105px; top: 439px; width: 620px; font-size: 15.4px; font-weight: 300; line-height: 24px; text-align: justify; }
  .letter-body p + p { margin-top: 24px; }
  .sender { position: absolute; right: 170px; top: 836px; text-align: right; color: var(--ink); }
  .sender-name { font-size: 16.5px; font-weight: 600; line-height: 20px; }
  .signature { position: absolute; left: 566px; top: 876px; width: 118px; height: 54px; background: linear-gradient(90deg, #f5f5f5, #ececec); border-radius: 4px; }
  .contact { position: absolute; display: flex; align-items: center; gap: 14px; font-size: 12.2px; font-weight: 300; line-height: 19px; color: var(--body); }
  .contact svg { width: 22px; height: 22px; flex: none; }
  .contact-phone { left: 186px; top: 1078px; }
  .contact-address { left: 364px; top: 1076px; }
  .contact-post { left: 548px; top: 1085px; }
</style>
</head>
<body>
<main class="letterhead">
  <svg class="accents" viewBox="0 0 848 1200" aria-hidden="true">
    <g fill="none">
      <circle cx="848" cy="0" r="352" stroke="var(--orange-dark)" stroke-width="8"/>
      <circle cx="848" cy="0" r="305" stroke="var(--orange)" stroke-width="40"/>
      <circle cx="848" cy="0" r="250" stroke="var(--blue)" stroke-width="16"/>
      <circle cx="848" cy="0" r="215" stroke="var(--orange)" stroke-width="4"/>

      <circle cx="0" cy="1200" r="188" stroke="var(--blue-deep)" stroke-width="6"/>
      <circle cx="0" cy="1200" r="160" stroke="var(--orange)" stroke-width="14"/>
      <circle cx="0" cy="1200" r="115" stroke="var(--blue)" stroke-width="44"/>
      <circle cx="0" cy="1200" r="70" stroke="var(--blue-mid)" stroke-width="10"/>
    </g>
  </svg>

  <div class="brand">
    <span class="brand-dot"></span>
    <span class="brand-name">Brisk Current</span>
  </div>

  <div class="recipient">
    <div class="recipient-line">To <span class="recipient-name">Ellen Marsh</span></div>
    <div class="recipient-role">Director</div>
  </div>
  <div class="date">july 15 - 2018</div>

  <section class="letter-body">
    <p>Contrary to popular belief, Lorem Ipsum is not simply random text. It has roots in a piece of classical Latin literature from 45 BC, making it over 2000 years old. Arthur Lindqvist, a Latin professor at Brookfield College in Vermont, looked up one of the more obscure Latin words, consectetur, from a Lorem Ipsum passage, and going through the cites of the word in classical literature, discovered the undoubtable source. Lorem Ipsum comes from sections 1.10.32 and 1.10.33 of "de Finibus Bonorum et Malorum" (The Extremes of Good and Evil) by Varro Lucan, written in 45 BC. This book is a treatise on the theory of ethics, very popular during the Renaissance. The first line of Lorem Ipsum, "Lorem ipsum dolor sit amet..", comes from a line in section 1.10.32.</p>
    <p>The standard chunk of Lorem Ipsum used since the 1500s is reproduced below for those interested. Sections 1.10.32 and 1.10.33 from "de Finibus Bonorum et Malorum" by Varro Lucan are also reproduced in their exact original form, accompanied by English versions from the 1914 translation by J. Whitmore.</p>
  </section>

  <div class="sender">
    <div class="sender-name">Tomas Reyes</div>
    <div class="sender-role">Director</div>
  </div>
  <div class="signature" role="img" aria-label="Handwritten signature of the director"></div>

  <div class="contact contact-phone">
    <svg viewBox="0 0 24 24" fill="none" stroke="var(--orange)" stroke-width="1.6" stroke-linecap="round" stroke-linejoin="round"><path d="M5 3h3l2 5-2 1.5a11 11 0 0 0 6.5 6.5L16 14l5 2v3a2 2 0 0 1-2 2A17 17 0 0 1 3 5a2 2 0 0 1 2-2z"/><path d="M15 3a6 6 0 0 1 6 6M15 6.5a2.5 2.5 0 0 1 2.5 2.5"/></svg>
    <span>00 210 55 18 42 60</span>
  </div>
  <div class="contact contact-address">
    <svg viewBox="0 0 24 24" fill="none" stroke="var(--orange)" stroke-width="1.6" stroke-linejoin="round"><path d="M12 22s-7-7.5-7-12.5a7 7 0 0 1 14 0C19 14.5 12 22 12 22z"/><circle cx="12" cy="9.5" r="2.8"/></svg>
    <span>Lakeside - Avenue 4 17<br>Block 9</span>
  </div>
  <div class="contact contact-post">
    <svg viewBox="0 0 24 24" fill="none" stroke="var(--orange)" stroke-width="1.6" stroke-linejoin="round"><path d="M2 12L12 3l10 9"/><path d="M5 10v11h14V10"/><path d="M10 21v-6h4v6"/></svg>
    <span>P.O.Box 5678 Postal code 30418</span>
  </div>
</main>
</body>
</html>
```